Design business cards for musician - Saxophone - Logo available

Hi all,

I want to have a new business card. I'm a professional saxophone player. I already have a logo and want that one in my business cards.

The colours that i've used in my logo are:

Blue: #0EBBD9
Black: #000000

In the business cards you're free to use other colors

I want to have the following credentials:

Name
Email
Telephone number
Website

```html
<!DOCTYPE html>
<html lang="en">
<head>
<meta charset="utf-8">
<title>Corvin – Business Cards</title>
<link rel="stylesheet" href="https://fonts.googleapis.com/css2?family=Roboto:wght@400;500&display=swap">
<style>
  :root {
    --sax-blue: #2bb8d6;
    --sax-blue-soft: #6fcbe0;
    --sax-blue-tint: #8fd8e8;
    --ink: #000000;
    --paper: #ffffff;
    --stage: #2a2c30;
    --text-light: #f2f2f2;
  }
  * { box-sizing: border-box; margin: 0; padding: 0; }
  html, body { width: 1200px; height: 900px; overflow: hidden; }
  body {
    background: var(--stage);
    font-family: "Roboto", Arial, sans-serif;
    position: relative;
  }
  .card {
    position: absolute;
    width: 340px;
    height: 580px;
    border-radius: 26px;
    overflow: hidden;
    background: var(--paper);
  }

  /* Contact side */
  .card--contact { left: 180px; top: 160px; }
  .contact__top {
    position: absolute; left: 0; top: 0; width: 100%; height: 320px;
    background: var(--sax-blue);
  }
  .contact__name {
    position: absolute; left: 150px; top: 34px;
    font-size: 22px; font-weight: 400; color: var(--ink); letter-spacing: 0.5px;
  }
  .contact__role {
    position: absolute; left: 150px; top: 64px;
    font-size: 10px; color: var(--ink); letter-spacing: 0.5px;
  }
  .contact__notes {
    position: absolute; left: 0; top: 96px; width: 100%; height: 210px;
    background:
      radial-gradient(ellipse 55% 45% at 30% 40%, var(--sax-blue-tint), transparent 70%),
      radial-gradient(ellipse 50% 45% at 72% 65%, var(--sax-blue-soft), transparent 70%),
      var(--sax-blue);
  }
  .contact__strip {
    position: absolute; left: 0; top: 320px; width: 70px; height: 260px;
    background: var(--sax-blue);
  }
  .contact__tile {
    position: absolute; left: 0; width: 70px; height: 58px;
    background: linear-gradient(180deg, var(--sax-blue), var(--sax-blue-soft));
  }
  .contact__tile-rule {
    position: absolute; left: 0; width: 70px; height: 6px; background: var(--paper);
  }
  .contact__panel {
    position: absolute; left: 70px; top: 320px; width: 270px; height: 260px;
    background: var(--ink);
  }
  .contact__logo-block {
    position: absolute; left: 200px; top: 320px; width: 140px; height: 130px;
    background: var(--paper);
    display: flex; align-items: center; justify-content: center;
  }
  .brand-name {
    font-family: "Roboto", Arial, sans-serif;
    font-weight: 400; color: var(--ink);
    display: flex; align-items: center; gap: 8px;
  }
  .brand-name__dot {
    width: 12px; height: 12px; border-radius: 50%; background: var(--sax-blue);
  }
  .contact__logo-block .brand-name { font-size: 26px; }
  .contact__list {
    position: absolute; left: 86px; top: 470px; list-style: none;
  }
  .contact__item {
    display: flex; align-items: center; gap: 10px;
    color: var(--text-light); font-size: 13px; margin-bottom: 12px;
    white-space: nowrap;
  }
  .contact__item svg { width: 18px; height: 18px; flex: none; }

  /* Logo side */
  .card--logo { left: 700px; top: 160px; }
  .logo__band {
    position: absolute; top: 0; width: 44px; height: 100%; background: var(--sax-blue);
  }
  .logo__band--left { left: 0; }
  .logo__band--right { right: 0; }
  .logo__mark {
    position: absolute; left: 50%; top: 50%;
    transform: translate(-50%, -50%) rotate(90deg);
  }
  .card--logo .brand-name { font-size: 54px; gap: 14px; }
  .card--logo .brand-name__dot { width: 22px; height: 22px; }
</style>
</head>
<body>

<section class="card card--contact" aria-label="Business card, contact side">
  <div class="contact__top"></div>
  <div class="contact__notes" role="img" aria-label="Pattern of pale music notes on blue"></div>
  <p class="contact__name">MARA QUILL</p>
  <p class="contact__role">CEO MANAGER</p>

  <div class="contact__strip" role="img" aria-label="Column of pale music notes in framed tiles">
    <div class="contact__tile" style="top:0"></div>
    <div class="contact__tile-rule" style="top:60px"></div>
    <div class="contact__tile" style="top:66px"></div>
    <div class="contact__tile-rule" style="top:126px"></div>
    <div class="contact__tile" style="top:132px"></div>
    <div class="contact__tile-rule" style="top:192px"></div>
    <div class="contact__tile" style="top:198px; height:62px"></div>
  </div>

  <div class="contact__panel"></div>
  <div class="contact__logo-block">
    <span class="brand-name"><span class="brand-name__dot"></span>Corvin</span>
  </div>

  <ul class="contact__list">
    <li class="contact__item">
      <svg viewBox="0 0 20 20"><circle cx="10" cy="10" r="9" fill="none" stroke="#2bb8d6" stroke-width="1.6"/><path d="M7 5.5l2 2-1 1.2c.6 1.3 1.6 2.3 2.9 2.9l1.2-1 2 2-1.3 1.4C9.5 13.6 6.4 10.5 5.6 6.8z" fill="#2bb8d6"/></svg>
      00-0031862294
    </li>
    <li class="contact__item">
      <svg viewBox="0 0 20 20"><rect x="2" y="5" width="16" height="11" fill="#2bb8d6"/><path d="M2 5l8 6 8-6" fill="none" stroke="#000" stroke-width="1.3"/></svg>
      mara@corvinsax.com
    </li>
    <li class="contact__item">
      <svg viewBox="0 0 20 20"><path d="M10 2l8 8h-3v7H5v-7H2z" fill="#2bb8d6"/></svg>
      Lisbon, Portugal
    </li>
  </ul>
</section>

<section class="card card--logo" aria-label="Business card, logo side">
  <div class="logo__band logo__band--left"></div>
  <div class="logo__band logo__band--right"></div>
  <div class="logo__mark">
    <span class="brand-name"><span class="brand-name__dot"></span>Corvin</span>
  </div>
</section>

</body>
</html>
```